Plakat-Design für Tanzkurse in Salsa, Bachata, Kizomba & Zouk
Zielgruppe
Tanzkurse in Salsa, Bachata, Kizomba & Zouk
Zielgruppe 20-45 Arbeitstätig & Studenten
Wir bieten in den oben genannten Tänzen mit Spezialisierten internationalen Trainern und Trainerinnen didaktisch & methodisch hochwertige Tanzkurse an.
Aufgabenstellung
Inhalte:
DIN A1
Es soll auf Gutscheine 'Tanzgutscheine' zu Weihnachten hingewiesen werden und Lust auf einen Tanzkurs bei uns machen.
Es soll edel, professionell, und farblich harmonisch sein. Keine Chilis, kein Kuban Feeling!
Mögliches Bildmaterial ist im Anhang zu finden.
Farbe Logo: #A82068
Weitere verwendete Farben: #0A8694

```html
<!DOCTYPE html>
<html lang="de">
<head>
<meta charset="utf-8">
<title>Tanzkurse – Ritmo Vivo</title>
<link href="https://fonts.googleapis.com/css2?family=Barlow:wght@400;500;600&family=Barlow+Condensed:wght@400;500;600&display=swap" rel="stylesheet">
<style>
  :root {
    --brand: #A82068;
    --brand-deep: #8e1a5a;
    --gold: #d9b36a;
    --gold-light: #f3dca4;
    --ink: #1c1a1e;
    --ink-soft: #3a3640;
    --white: #ffffff;
    --photo-top: #7f7287;
    --photo-mid: #c9bfcc;
    --photo-low: #efe9ef;
  }
  * { margin: 0; padding: 0; box-sizing: border-box; }
  html, body { width: 848px; height: 1200px; overflow: hidden; background: var(--white); }
  .poster {
    position: relative; width: 848px; height: 1200px; overflow: hidden;
    font-family: "Barlow", sans-serif; color: var(--ink);
  }
  .hero-photo {
    position: absolute; inset: 0;
    background:
      radial-gradient(ellipse at 70% 45%, rgba(255,240,245,0.55), rgba(255,255,255,0) 60%),
      linear-gradient(180deg, var(--photo-top) 0%, var(--photo-mid) 40%, var(--photo-low) 78%, #f7f4f7 100%);
  }
  .brand {
    position: absolute; top: 58px; left: 0; width: 100%;
    display: flex; flex-direction: column; align-items: center;
  }
  .brand-row { display: flex; align-items: center; gap: 14px; }
  .brand-name {
    font-family: "Barlow", sans-serif; font-weight: 500; font-size: 40px;
    color: var(--ink-soft); letter-spacing: 1px;
  }
  .brand-dot { width: 30px; height: 30px; border-radius: 50%; background: var(--brand); }
  .brand-tagline { margin-top: 4px; font-size: 15px; color: var(--ink-soft); letter-spacing: 0.5px; }
  .headline {
    position: absolute; top: 418px; left: 0; width: 100%; text-align: center;
    font-family: "Barlow Condensed", sans-serif; font-weight: 500; font-size: 94px;
    line-height: 1; color: var(--brand); letter-spacing: 1px;
  }
  .rule { position: absolute; left: 232px; width: 392px; height: 1.5px; background: rgba(255,255,255,0.9); }
  .rule-top { top: 550px; }
  .rule-bottom { top: 640px; }
  .styles {
    position: absolute; top: 575px; left: 0; width: 100%; text-align: center;
    font-family: "Barlow Condensed", sans-serif; font-weight: 500; font-size: 40px;
    color: var(--white); letter-spacing: 10px; line-height: 1;
  }
  .voucher { position: absolute; left: 84px; top: 742px; width: 274px; height: 274px; }
  .contact {
    position: absolute; right: 64px; top: 918px; text-align: right;
    font-size: 17px; line-height: 35px; color: var(--ink-soft);
  }
  .contact .school { font-weight: 600; color: var(--ink); }
  .contact .mail-phone { margin-top: 18px; }
  .website {
    position: absolute; bottom: 52px; left: 0; width: 100%; text-align: center;
    font-family: "Barlow Condensed", sans-serif; font-weight: 400; font-size: 62px;
    line-height: 1; color: var(--ink); letter-spacing: 0.5px;
  }
</style>
</head>
<body>
<main class="poster">
  <div class="hero-photo" role="img" aria-label="Foto eines lachenden Tanzpaares in hellem Raum, der Mann dreht die Frau unter erhobenem Arm"></div>

  <header class="brand">
    <div class="brand-row">
      <span class="brand-name">Ritmo Vivo</span>
      <span class="brand-dot"></span>
    </div>
    <div class="brand-tagline">Salsa · Bachata · Kizomba</div>
  </header>

  <h1 class="headline">TANZKURSE</h1>
  <div class="rule rule-top"></div>
  <p class="styles">SALSA • BACHATA • KIZOMBA</p>
  <div class="rule rule-bottom"></div>

  <svg class="voucher" viewBox="0 0 274 274" aria-label="Tanzgutschein zu Weihnachten">
    <defs>
      <linearGradient id="goldRing" x1="0" y1="0" x2="1" y2="1">
        <stop offset="0" stop-color="#f6e2ad"/>
        <stop offset="0.5" stop-color="#c99a4e"/>
        <stop offset="1" stop-color="#f3d99a"/>
      </linearGradient>
    </defs>
    <circle cx="137" cy="137" r="134" fill="url(#goldRing)"/>
    <circle cx="137" cy="137" r="127" fill="#ffffff"/>
    <circle cx="137" cy="137" r="122" fill="var(--brand-deep)"/>
    <g transform="rotate(-16 137 137)" font-family="Barlow Condensed, sans-serif" text-anchor="middle">
      <text x="137" y="92" font-size="27" fill="#ffffff" font-weight="500">Die Geschenkidee</text>
      <text x="137" y="121" font-size="27" fill="#ffffff" font-weight="500">zu Weihnachten:</text>
      <text x="137" y="160" font-size="25" fill="var(--gold-light)" font-weight="600" letter-spacing="1">TANZGUTSCHEIN</text>
      <text x="137" y="190" font-size="19" fill="#ffffff">Verschenke ein paar Stunden</text>
      <text x="137" y="212" font-size="19" fill="#ffffff">gemeinsamen Spaß.</text>
    </g>
  </svg>

  <address class="contact" style="font-style: normal;">
    <div class="school">Tanzschule Ritmo Vivo</div>
    <div>Lindenweg 14 &amp; weitere Locations</div>
    <div>79100 Musterstadt</div>
    <div class="mail-phone">info@ritmo-vivo-tanz.de | T +49 151 000 123 45</div>
  </address>

  <p class="website">WWW.RITMO-VIVO-TANZ.DE</p>
</main>
</body>
</html>
```